immediate money for financial solutions

We need a Clean yet, eye catching, Business Card denoting a professional financial/tech firm. The front should have our logo and the notion that we are money lenders that get business loans quickly & easily. Maybe shade the colors of our logo. We are opened, but not committed to an unusual shaped card. The Back Should have our Business Contact Info & logo found on our website's front page: KORVANTINC.COM

Financial

```html
<!DOCTYPE html>
<html lang="en">
<head>
<meta charset="utf-8">
<title>Korvant Inc — Business Card</title>
<link rel="stylesheet" href="https://fonts.googleapis.com/css2?family=Exo+2:wght@400;500;600&display=swap">
<style>
  :root {
    --backdrop: #e9ece9;
    --card-white: #ffffff;
    --brand-green: #2ea64a;
    --accent-teal: #84c8b6;
    --logo-green: #2f9a4f;
    --ink-light: #ffffff;
  }
  html, body {
    margin: 0;
    padding: 0;
    width: 1200px;
    height: 900px;
    overflow: hidden;
    background: var(--backdrop);
    font-family: "Exo 2", "Segoe UI", sans-serif;
  }
  .canvas {
    position: relative;
    width: 1200px;
    height: 900px;
  }
  .business-card {
    position: absolute;
    left: 75px;
    top: 150px;
    width: 1050px;
    height: 600px;
    border-radius: 56px;
    overflow: hidden;
    background: var(--card-white);
    box-shadow: 0 14px 40px rgba(0, 0, 0, 0.12);
  }
  .card-shapes {
    position: absolute;
    inset: 0;
  }
  .brand {
    position: absolute;
    left: 90px;
    top: 275px;
    display: flex;
    flex-direction: column;
    align-items: flex-start;
    gap: 10px;
  }
  .brand-row {
    display: flex;
    align-items: center;
    gap: 14px;
  }
  .brand-square {
    width: 30px;
    height: 30px;
    background: var(--logo-green);
  }
  .brand-name {
    font-size: 44px;
    font-weight: 600;
    color: var(--logo-green);
    letter-spacing: 1px;
  }
  .brand-tagline {
    font-size: 19px;
    font-weight: 500;
    color: var(--logo-green);
    letter-spacing: 2px;
    padding-left: 46px;
  }
  .contact {
    position: absolute;
    right: 60px;
    top: 60px;
    text-align: right;
    color: var(--ink-light);
  }
  .person-name {
    font-size: 30px;
    font-weight: 500;
    letter-spacing: 2px;
    margin: 0;
  }
  .person-title {
    font-size: 18px;
    letter-spacing: 2px;
    margin: 6px 0 0;
  }
  .address {
    margin: 70px 0 0;
    font-size: 22px;
    line-height: 32px;
    letter-spacing: 1px;
  }
  .contact-list {
    list-style: none;
    margin: 36px 0 0;
    padding: 0;
    font-size: 21px;
    letter-spacing: 1px;
  }
  .contact-list li {
    display: flex;
    justify-content: flex-end;
    align-items: center;
    gap: 12px;
    height: 40px;
  }
  .contact-icon {
    width: 22px;
    height: 22px;
    fill: none;
    stroke: var(--ink-light);
    stroke-width: 2;
    stroke-linecap: round;
    stroke-linejoin: round;
  }
</style>
</head>
<body>
<main class="canvas">
  <section class="business-card">
    <svg class="card-shapes" width="1050" height="600" viewBox="0 0 1050 600" aria-hidden="true">
      <path d="M250 0 C470 60 560 260 500 600 L1050 600 L1050 0 Z" fill="var(--accent-teal)"/>
      <path d="M290 0 C510 60 600 260 540 600 L1050 600 L1050 0 Z" fill="var(--brand-green)"/>
    </svg>

    <div class="brand">
      <div class="brand-row">
        <span class="brand-square"></span>
        <span class="brand-name">KORVANT INC</span>
      </div>
      <span class="brand-tagline">FAST BUSINESS LOANS</span>
    </div>

    <div class="contact">
      <p class="person-name">DANA WHITFORD</p>
      <p class="person-title">PRESIDENT</p>
      <p class="address">214, 9th floor,<br>Harbor Way Central</p>
      <ul class="contact-list">
        <li>012 345 6789
          <svg class="contact-icon" viewBox="0 0 24 24"><path d="M5 3h4l2 5-2.5 1.5a11 11 0 0 0 6 6L16 13l5 2v4a2 2 0 0 1-2 2A17 17 0 0 1 3 5a2 2 0 0 1 2-2z"/></svg>
        </li>
        <li>012 345 6789
          <svg class="contact-icon" viewBox="0 0 24 24"><rect x="7" y="2" width="10" height="20" rx="2"/><path d="M11 18h2"/></svg>
        </li>
        <li>012 345 6789
          <svg class="contact-icon" viewBox="0 0 24 24"><rect x="3" y="9" width="18" height="12" rx="1"/><path d="M7 9V3h10v6M7 13h4M7 17h4"/></svg>
        </li>
        <li>hello@korvantinc.com
          <svg class="contact-icon" viewBox="0 0 24 24"><rect x="3" y="5" width="18" height="14" rx="1"/><path d="M3 6l9 7 9-7"/></svg>
        </li>
        <li>www.korvantinc.com
          <svg class="contact-icon" viewBox="0 0 24 24"><circle cx="12" cy="12" r="9"/><path d="M3 12h18M12 3c3 3 3 15 0 18M12 3c-3 3-3 15 0 18"/></svg>
        </li>
      </ul>
    </div>
  </section>
</main>
</body>
</html>
```